Harrowgate - Pell Corporate PowerPoint Presentation Template

A custom, corporate template that is highly professional, neat/crisp, "serious," and captures/emphasizes the essence of a global, mutli-brand consumer products company that has deep tradition and values family, hard work, performance, innovation, and service to our consumers and retail partners.
The company's roots and headquarters are in Texas. We are a private and family owned since our founding almost 100 years ago. The corporate website is www.hpvcorp-example.com and other branded websites can be accessed from this site.
Our current presentation title page is attached. We believe it to be somewhat stale/out of date and less sophisticated that the image we'd prefer to project. We occasionally add/change logos and will have to adapt the presentation. These presentations must look good printed.
Please contact me with any questions or requests and I will respond very quickly.
Target Market(s)
Corporate Executives
Industry/Entity Type
It Professional
Requirements
Must have
- Sans Serif font (can't select below). Industry is Apparel and Footwear / Consumer Products (can't select below).

```html
<!DOCTYPE html>
<html lang="pt">
<head>
<meta charset="utf-8">
<title>Harrowgate - Pell — Gráfico</title>
<link href="https://fonts.googleapis.com/css2?family=Arimo:wght@400;700&display=swap" rel="stylesheet">
<style>
  :root {
    --brand-blue: #0051a2;
    --brand-green: #138a4f;
    --ink: #595959;
    --grid: #d9d9d9;
    --series-1: #4a7eb1;
    --series-2: #5b9bd5;
    --series-3: #a9c5e6;
    --map-tone: #e6e9f1;
    --paper: #ffffff;
  }
  html, body { margin: 0; padding: 0; overflow: hidden; }
  body { width: 1200px; height: 900px; background: var(--paper); font-family: "Arimo", Arial, sans-serif; }
  .slide { position: relative; width: 1200px; height: 900px; overflow: hidden; background: var(--paper); }
  .header-band { position: absolute; left: 169px; top: 0; width: 1031px; height: 94px; background: var(--brand-blue); }
  .brand-area {
    position: absolute; left: 0; top: 0; width: 169px; height: 94px;
    display: flex; align-items: center; justify-content: center; z-index: 2;
  }
  .brand-name {
    width: 140px; text-align: center;
    font-size: 17px; line-height: 21px; font-weight: 700; color: var(--brand-blue);
  }
  .brand-name span { display: block; white-space: nowrap; }
  .rule { position: absolute; left: 0; width: 1200px; background: var(--brand-green); }
  .rule-top { top: 97px; height: 9px; }
  .rule-bottom { top: 853px; height: 9px; }
  .footer-band { position: absolute; left: 0; top: 862px; width: 1200px; height: 38px; background: var(--brand-blue); }
  .footer-url { position: absolute; left: 24px; top: 872px; font-size: 18px; color: var(--paper); }
  .world-map {
    position: absolute; left: 0; top: 150px; width: 1180px; height: 670px;
    background: radial-gradient(ellipse at 50% 45%, var(--map-tone) 0%, rgba(230,233,241,0.5) 45%, rgba(255,255,255,0) 75%);
  }
  .chart { position: absolute; left: 0; top: 0; }
  .chart text { font-family: "Arimo", Arial, sans-serif; fill: var(--ink); }
  .chart-title { font-size: 28px; }
  .axis-label { font-size: 17px; }
  .gridline { stroke: var(--grid); stroke-width: 1; }
  .s1 { fill: var(--series-1); }
  .s2 { fill: var(--series-2); }
  .s3 { fill: var(--series-3); }
</style>
</head>
<body>
<div class="slide">
  <div class="header-band"></div>
  <div class="brand-area">
    <div class="brand-name"><span>Harrowgate -</span><span>Pell</span></div>
  </div>
  <div class="rule rule-top"></div>

  <div class="world-map" role="img" aria-label="Faint dotted world map in the background"></div>

  <svg class="chart" width="1200" height="900" viewBox="0 0 1200 900">
    <text class="chart-title" x="600" y="193" text-anchor="middle">Título do Gráfico</text>

    <g class="grid">
      <line class="gridline" x1="144" y1="223.6" x2="1100" y2="223.6"/>
      <line class="gridline" x1="144" y1="299" x2="1100" y2="299"/>
      <line class="gridline" x1="144" y1="374.4" x2="1100" y2="374.4"/>
      <line class="gridline" x1="144" y1="449.8" x2="1100" y2="449.8"/>
      <line class="gridline" x1="144" y1="525.2" x2="1100" y2="525.2"/>
      <line class="gridline" x1="144" y1="600.6" x2="1100" y2="600.6"/>
      <line class="gridline" x1="144" y1="676" x2="1100" y2="676"/>
    </g>

    <g class="y-axis" text-anchor="end">
      <text class="axis-label" x="104" y="682">0</text>
      <text class="axis-label" x="104" y="607">1</text>
      <text class="axis-label" x="104" y="531">2</text>
      <text class="axis-label" x="104" y="456">3</text>
      <text class="axis-label" x="104" y="380">4</text>
      <text class="axis-label" x="104" y="305">5</text>
      <text class="axis-label" x="104" y="230">6</text>
    </g>

    <g class="bars">
      <rect class="s1" x="169" y="351.8" width="43" height="324.2"/>
      <rect class="s2" x="221" y="495" width="43" height="181"/>
      <rect class="s3" x="276" y="525.2" width="43" height="150.8"/>

      <rect class="s1" x="412" y="487.5" width="43" height="188.5"/>
      <rect class="s2" x="466" y="344.2" width="43" height="331.8"/>
      <rect class="s3" x="520" y="525.2" width="43" height="150.8"/>

      <rect class="s1" x="656" y="412.1" width="43" height="263.9"/>
      <rect class="s2" x="710" y="540.3" width="43" height="135.7"/>
      <rect class="s3" x="764" y="449.8" width="43" height="226.2"/>

      <rect class="s1" x="900" y="336.7" width="43" height="339.3"/>
      <rect class="s2" x="954" y="464.9" width="43" height="211.1"/>
      <rect class="s3" x="1008" y="299" width="43" height="377"/>
    </g>

    <g class="x-axis" text-anchor="middle">
      <text class="axis-label" x="243" y="707">Categoria 1</text>
      <text class="axis-label" x="487" y="707">Categoria 2</text>
      <text class="axis-label" x="731" y="707">Categoria 3</text>
      <text class="axis-label" x="975" y="707">Categoria 4</text>
    </g>

    <g class="legend">
      <rect class="s1" x="469" y="733" width="10" height="10"/>
      <text class="axis-label" x="484" y="744">Série 1</text>
      <rect class="s2" x="565" y="733" width="10" height="10"/>
      <text class="axis-label" x="580" y="744">Série 2</text>
      <rect class="s3" x="661" y="733" width="10" height="10"/>
      <text class="axis-label" x="676" y="744">Série 3</text>
    </g>
  </svg>

  <div class="rule rule-bottom"></div>
  <div class="footer-band"></div>
  <div class="footer-url">http://www.hpvcorp-example.com/</div>
</div>
</body>
</html>
```